High end boutique food product label

We are looking for a label design to be used on our range of high end food products. We don't have a design or colour scheme in mind and are interested to see what ideas are submitted.
We would like it to feel sophisticated, chic, and eye-catching.
All of our products are handmade in Australia using Australian ingredients.
The graphics for the label will need to be scaleable to be fit a variety of labels from small squat jars with labels sized 3.5cm high and 7cm wide, to tall thin bottles with labels that are 14cm high and 4.5cm wide.
We would be interested in working with the winning designer to create these different sized labels.
The label submitted for this project should be 14cm high and 4.5cm wide, it should include our logo (file supplied in .jpeg and .ai), the product name 'Extra Virgin Olive Oil' and the size '250ml'.
This is just the front label on a bottle, we are not expecting a rear label to be created currently.
You are welcome to use any fonts you think will look good but the fonts used in our logo are Allaina Medium and Bebas Kai Regular.

```html
<!DOCTYPE html>
<html lang="en">
<head>
<meta charset="utf-8">
<title>Wren &amp; Hale – Extra Virgin Olive Oil Labels</title>
<link href="https://fonts.googleapis.com/css2?family=Rufina:wght@400;700&display=swap" rel="stylesheet">
<style>
  :root {
    --olive: #2d3a1e;
    --olive-soft: #3a4a28;
    --crimson: #9b1b25;
    --sand: #c0a983;
    --sand-light: #d9c9a6;
    --paper: #ffffff;
    --cream: #f4ecdc;
    --stage: #f1ead9;
  }
  * { margin: 0; padding: 0; box-sizing: border-box; }
  html, body {
    width: 686px; height: 1200px; overflow: hidden;
    background: var(--stage);
    font-family: "Rufina", Georgia, serif;
  }
  .canvas { position: relative; width: 686px; height: 1200px; }

  .label { position: absolute; overflow: hidden; background: var(--sand); }
  .label__field { position: absolute; left: 0; right: 0; top: 0; background: var(--olive); }
  .label__pattern {
    position: absolute;
    background: linear-gradient(180deg, var(--olive) 0%, var(--olive-soft) 50%, var(--olive) 100%);
  }
  .label__brand {
    position: absolute; top: 0; background: var(--crimson);
    display: flex; align-items: center; justify-content: center;
    text-align: center; color: var(--cream); font-weight: 700; line-height: 1.05;
  }
  .label__panel {
    position: absolute; background: var(--paper);
  }
  .label__frame {
    position: absolute; border: 1px solid var(--olive);
  }
  .label__title {
    position: absolute; left: 0; right: 0; text-align: center;
    color: var(--olive); font-weight: 700; line-height: 1.02;
    text-shadow: 1px 1px 0 var(--sand);
  }
  .label__sprig {
    position: absolute;
    background: linear-gradient(160deg, rgba(217,201,166,0) 0%, rgba(217,201,166,.55) 60%, rgba(192,169,131,.45) 100%);
  }
  .label__size { position: absolute; left: 0; right: 0; text-align: center; color: var(--olive); }

  /* Tall bottle label */
  .label--bottle { left: 17px; top: 276px; width: 208px; height: 647px; }
  .label--bottle .label__field { height: 360px; }
  .label--bottle .label__pattern { left: 0; right: 0; top: 95px; height: 127px; }
  .label--bottle .label__brand { left: 57px; width: 95px; height: 132px; font-size: 17px; padding-top: 14px; }
  .label--bottle .label__panel { left: 21px; top: 236px; width: 166px; height: 323px; border-radius: 16px; }
  .label--bottle .label__frame { inset: 8px; border-radius: 10px; }
  .label--bottle .label__title { top: 20px; font-size: 41px; }
  .label--bottle .label__sprig { left: 0; right: 0; bottom: 2px; height: 122px; border-radius: 0 0 14px 14px; }
  .label--bottle .label__size { top: 573px; font-size: 16px; }

  /* Squat jar label */
  .label--jar { left: 262px; top: 276px; width: 408px; height: 204px; }
  .label--jar .label__field { height: 114px; }
  .label--jar .label__pattern { left: 94px; right: 0; top: 0; height: 114px; }
  .label--jar .label__brand { left: 0; width: 94px; height: 204px; font-size: 15px; }
  .label--jar .label__panel { left: 148px; top: 45px; width: 203px; height: 106px; border-radius: 12px; }
  .label--jar .label__frame { inset: 7px; border-radius: 8px; }
  .label--jar .label__title { top: 14px; font-size: 25px; }
  .label--jar .label__sprig { right: 2px; bottom: 2px; width: 90px; height: 52px; border-radius: 0 0 10px 0; }
  .label--jar .label__size { top: 163px; font-size: 14px; }
</style>
</head>
<body>
<main class="canvas">

  <section class="label label--bottle" aria-label="Bottle front label, 250ml">
    <div class="label__field"></div>
    <div class="label__pattern" role="img" aria-label="Dotted circle, leaf and droplet pattern in sand tones"></div>
    <div class="label__brand">Wren<br>&amp; Hale</div>
    <div class="label__panel">
      <div class="label__frame"></div>
      <h1 class="label__title">Extra<br>Virgin<br>Olive<br>Oil</h1>
      <div class="label__sprig" role="img" aria-label="Fine line sketch of an olive branch with fruit and blossoms"></div>
    </div>
    <p class="label__size">250ml</p>
  </section>

  <section class="label label--jar" aria-label="Jar wrap label, 50ml">
    <div class="label__field"></div>
    <div class="label__pattern" role="img" aria-label="Dotted circle, leaf and droplet pattern in sand tones"></div>
    <div class="label__brand">Wren<br>&amp; Hale</div>
    <div class="label__panel">
      <div class="label__frame"></div>
      <h2 class="label__title">Extra Virgin<br>Olive Oil</h2>
      <div class="label__sprig" role="img" aria-label="Fine line sketch of an olive sprig"></div>
    </div>
    <p class="label__size">50ml</p>
  </section>

</main>
</body>
</html>
```